Velvet Arc Car Detailing Brochure

I would like a trifold brochure designed for my car detailing business. The background has to be full black or mostly black with some designing using only colors present in our logo.

Front page must have our logo and name, list of services, a photo and mybe our phone number but no long text.

Inside I want to present each service one by one with its description and a photo representing/showing each service. (I will provide the text below). For photos, use stock photos and I will add come of mines already too.

On the back of the brochure I want to have contact & info: phone number, opening hours, address, website, Instagram.

Outside left I want the text About us and photo/design.

I want the brochure to be neat, professional, easy to read, but at the same time not too boring.

Text:
1. About us
a. the ultimate destination for car care in Geneva. We provide personalized, detail-oriented services that bring out the best in your car. With our expert techniques and dedicated approach, we ensure that your car receives the utmost care and attention. Experience a place where passion meets precision and let us create an exceptional car care experience designed just for you.
2. Services:

DETAILING & HAND WASH

• Comprehensive exterior & interior care
• Personalisation and tailored cleaning packages
• Decontamination
• Premium products
• Attention to detail for a perfect finish

POLISHING

• Eliminates scratches, holograms
• Revives and protects paint
• Ensures lasting gloss
• Enhances paint life
• Preserves car’s value and beauty

CERAMIC TREATMENT

• Durable paint protection
• Water-repellent (hydrophobic) effect
• Easier cleaning, enhanced shine
• Long-term surface safeguarding
• Shields against environmental impacts

DRY ICE WASH

• Innovative, waterless method
• Safe for all car parts
• Deep cleans, removes odors
• Allergen-free, antibacterial
• Gentle, effective
• Advanced cleaning technology

COVERING

• Personalized vehicle styling
• More than 150 colours available
• Clean cut without using a cutter
• High-quality, durable materials
• Custom designs available

PROTECTION FILM

• Invisible, durable shield
• Self-healing technology
• 10-year warranty by RQ FOLV

DETAILING BOUTIQUE

• Premium brands available
• Buy on site during your visit
• Granite Assembly, Pip Autos, DRAV Norra
• Essential for at-home car care
• Perfect for quick touch-ups
(for these three brands you can put their logos

Target Market(s)

Our target market includes car owners of all price ranges, with a special focus on those who are passionate about their vehicles. We cater to clients who value excellent service and results, and seek to maintain their cars in pristine condition.

Industry/Entity Type

Automobile / Car detailing

Colors

Designer to choose colors to be used in the design.

Requirements
Must have
• Brand Consistency: The brochure must adhere to our brand colors and style, particularly utilizing the colors present in our logo. Trifold Layout: The design must be specifically tailored for a trifold brochure format. Legibility: Text must be easy to read against the mostly black background, with appropriate font size and style. Professional Look and Feel: The overall design must convey professionalism while being engaging and not overly complex. Photo representation: each service description should have a phot presenting it.
Should not have
• Overcrowded Design: Avoid cluttering with too much text or too many images. The layout should be clean and easy to navigate. Cartoonish Fonts or Graphics: Avoid using unprofessional or casual fonts and graphics that do not align with the upscale and professional image of our business. Distracting Backgrounds: The background should complement and not overpower the content. Stick to the theme of mostly black with design elements from our logo.

```html
<!DOCTYPE html>
<html lang="en">
<head>
<meta charset="utf-8">
<title>Velvet Arc Car Detailing – Trifold Brochure</title>
<link href="https://fonts.googleapis.com/css2?family=Montserrat:wght@400;500;600;700&family=Great+Vibes&display=swap" rel="stylesheet">
<style>
:root{
  --pink:#c23a9e;
  --purple:#8a52c6;
  --blue:#2f7fd2;
  --black:#050505;
  --ink:#111;
  --white:#fff;
  --grey-bg:#a9a9ab;
  --paper:#f2f2f2;
  --grad:linear-gradient(90deg,var(--pink),var(--purple) 55%,var(--blue));
}
*{box-sizing:border-box;margin:0;padding:0}
html,body{width:875px;height:1200px;overflow:hidden}
body{background:var(--grey-bg);font-family:'Montserrat',sans-serif;color:var(--white);position:relative}
.sheet{position:absolute;left:77px;width:722px;height:520px;overflow:hidden;box-shadow:0 6px 18px rgba(0,0,0,.35)}
.sheet--outside{top:62px;background:var(--black)}
.sheet--inside{top:640px;background:var(--paper)}
.abs{position:absolute}
.script{font-family:'Great Vibes',cursive;font-weight:400;background:var(--grad);-webkit-background-clip:text;background-clip:text;color:transparent}

/* outside */
.about-title{left:34px;top:8px;font-size:52px;line-height:44px}
.about-title span{display:block;padding-left:96px;background:linear-gradient(90deg,#ddd,#8d8d8d);-webkit-background-clip:text;background-clip:text}
.about-text{left:24px;top:106px;width:192px;font-size:8.6px;line-height:12.2px;text-align:center}
.photo-circle{left:48px;top:246px;width:146px;height:146px;border-radius:50%;border:4px solid #e6e6e6;background:radial-gradient(circle at 45% 55%,#3a3a3a,#cfcfcf 60%,#8a8a8a)}

.contact{left:240px;top:0;width:241px;text-align:center;color:var(--ink);font-size:8.6px}
.contact .icon{position:absolute;left:112px;width:18px;height:18px}
.contact .line{position:absolute;left:0;width:241px}
.contact .bold{font-weight:700}
.hours{position:absolute;top:57px;left:24px;width:195px;display:flex;justify-content:space-between;line-height:14px;font-size:8.6px}
.hours div{text-align:center}

.cover-mark{left:565px;top:17px;width:70px;height:70px;border-radius:50%;border:4px solid var(--purple)}
.cover-name{left:481px;top:86px;width:241px;text-align:center;font-size:14px;letter-spacing:.5px}
.cover-head{left:481px;top:431px;width:241px;text-align:center;font-size:19.5px;line-height:19px;font-weight:500;background:var(--grad);-webkit-background-clip:text;background-clip:text;color:transparent}
.cover-tag{left:481px;top:472px;width:241px;text-align:center;font-size:11px;line-height:12px;font-weight:500}

/* inside */
.panel-black{background:var(--black)}
.services-title{left:28px;top:30px;font-size:60px;line-height:1}
.pill{position:absolute;left:29px;width:191px;height:23px;border-radius:12px;padding:1.5px;background:var(--grad)}
.pill span{display:flex;align-items:center;justify-content:center;width:100%;height:100%;border-radius:11px;background:var(--black);font-weight:700;font-size:10.8px;letter-spacing:.3px}
.card{position:absolute;background:var(--black);padding:6px 0 0 10px}
.card h3{font-family:'Great Vibes',cursive;font-weight:400;font-size:15px;line-height:14px;background:var(--grad);-webkit-background-clip:text;background-clip:text;color:transparent;display:inline-block}
.ticks{list-style:none;margin-top:2px;font-size:8.1px;line-height:9.2px;width:138px}
.card--right .ticks{width:128px}
.ticks li{position:relative;padding-left:9px;margin-bottom:2.6px}
.ticks li::before{content:"";position:absolute;left:0;top:2px;width:3px;height:5px;border:solid var(--pink);border-width:0 1.3px 1.3px 0;transform:rotate(40deg)}
.card .pic{position:absolute;top:14px;width:82px;height:83px;border:1px solid #ddd}
.card--mid .pic{left:152px}
.card--right .pic{left:150px}
.brands{margin-top:2px;padding-left:9px;font-size:9.5px;line-height:11px;font-weight:700}
.strip{position:absolute;top:385px;height:115px}
</style>
</head>
<body>

<section class="sheet sheet--outside">
  <svg class="abs" width="722" height="520" viewBox="0 0 722 520" style="left:0;top:0">
    <defs>
      <linearGradient id="paperGrad" x1="0" y1="0" x2="0" y2="1">
        <stop offset="0" stop-color="#fff"/><stop offset="1" stop-color="#dedede"/>
      </linearGradient>
      <linearGradient id="bandGrad" x1="0" y1="0" x2="1" y2="1">
        <stop offset="0" stop-color="#b0349b"/><stop offset=".55" stop-color="#8a52c6"/><stop offset="1" stop-color="#2f7fd2"/>
      </linearGradient>
      <linearGradient id="carGrad" x1="0" y1="0" x2="1" y2="1">
        <stop offset="0" stop-color="#2a2a2c"/><stop offset=".5" stop-color="#121214"/><stop offset="1" stop-color="#3a3d44"/>
      </linearGradient>
      <linearGradient id="coverGrad" x1="0" y1="0" x2="1" y2="1">
        <stop offset="0" stop-color="#0c0d12"/><stop offset=".45" stop-color="#2e3b55"/><stop offset=".75" stop-color="#1a1f2c"/><stop offset="1" stop-color="#050506"/>
      </linearGradient>
    </defs>
    <rect x="240" y="0" width="241" height="520" fill="url(#paperGrad)"/>
    <path d="M240 130 C300 210 420 210 481 130" fill="none" stroke="#ecd6e8" stroke-width="4"/>
    <path d="M0 318 C200 296 400 330 481 515 L481 520 L466 520 C330 360 180 336 0 360 Z" fill="url(#bandGrad)"/>
    <path role="img" aria-label="Photo: front of a black sports car with water droplets" d="M0 360 C180 336 330 360 466 520 L0 520 Z" fill="url(#carGrad)"/>
    <rect role="img" aria-label="Photo: dark blue sports car rear with red tail lights" x="481" y="0" width="241" height="520" fill="url(#coverGrad)"/>
  </svg>

  <h1 class="abs about-title script">About<span>Us</span></h1>
  <p class="abs about-text">The ultimate destination for car care in Geneva. We provide personalized, detail-oriented services that bring out the best in your car. With our expert techniques and dedicated approach, we ensure that your car receives the utmost care and attention. Experience a place where passion meets precision and let us create an exceptional car care experience designed just for you.</p>
  <div class="abs photo-circle" role="img" aria-label="Photo: interior console being polished with a small machine"></div>

  <div class="abs contact">
    <svg class="icon" style="top:25px" viewBox="0 0 20 20" fill="none" stroke="#a94fc0" stroke-width="1.6"><circle cx="10" cy="10" r="8" stroke-dasharray="38 6"/><path d="M10 5v5l3 2"/></svg>
    <div class="line bold" style="top:44px">Opening Time Visit Us</div>
    <div class="hours"><div>Monday – Friday<br>8:00am – 5:00pm</div><div>Saturday – Closed<br>Sunday – Closed</div></div>
    <svg class="icon" style="top:97px" viewBox="0 0 20 20" fill="none" stroke="#a94fc0" stroke-width="1.6"><path d="M3 9l7-6 7 6v8H3z"/><path d="M8 17v-5h4v5"/></svg>
    <div class="line" style="top:116px">St Name Here, 000 City Name, ES</div>
    <svg class="icon" style="top:139px" viewBox="0 0 20 20" fill="none" stroke="#a94fc0" stroke-width="1.6"><rect x="2" y="4" width="16" height="12" rx="2"/><path d="M2 6l8 6 8-6"/></svg>
    <div class="line" style="top:157px">mara@velvetarc.ch</div>
    <svg class="icon" style="top:212px" viewBox="0 0 20 20" fill="none" stroke="#a94fc0" stroke-width="1.6"><path d="M5 3l3 3-2 2c1 2 3 4 5 5l2-2 3 3-2 3C8 16 4 12 3 5z"/><path d="M12 3a5 5 0 0 1 5 5M12 6a2 2 0 0 1 2 2"/></svg>
    <div class="line bold" style="top:231px">+41765550123</div>
    <svg class="icon" style="top:253px" viewBox="0 0 20 20"><circle cx="10" cy="10" r="7" fill="none" stroke="#a94fc0" stroke-width="1.8"/></svg>
    <div class="line" style="top:272px">instagrammara@velvetarc.ch</div>
    <svg class="icon" style="top:294px" viewBox="0 0 20 20" fill="none" stroke="#a94fc0" stroke-width="1.6"><circle cx="10" cy="10" r="8"/><path d="M2 10h16M10 2c3 3 3 13 0 16M10 2c-3 3-3 13 0 16"/></svg>
    <div class="line bold" style="top:313px">www.velvetarc.ch</div>
  </div>

  <div class="abs cover-mark"></div>
  <div class="abs cover-name">VELVET ARC</div>
  <h2 class="abs cover-head">CAR DETAILING<br>&amp; WASH</h2>
  <p class="abs cover-tag">MAKING PEOPLE SUCCESSFUL<br>IN A CHANGING WORLD</p>
</section>

<section class="sheet sheet--inside">
  <div class="abs panel-black" style="left:0;top:17px;width:240px;height:360px">
    <h2 class="abs services-title script">Services</h2>
    <div class="pill" style="top:93px"><span>DETAILING &amp; HAND WASH</span></div>
    <div class="pill" style="top:130px"><span>POLISHING</span></div>
    <div class="pill" style="top:166px"><span>CERAMIC TREATMENT</span></div>
    <div class="pill" style="top:203px"><span>DRY ICE WASH</span></div>
    <div class="pill" style="top:239px"><span>COVERING</span></div>
    <div class="pill" style="top:276px"><span>PROTECTION FILM</span></div>
    <div class="pill" style="top:313px"><span>DETAILING BOUTIQUE</span></div>
  </div>

  <article class="card card--mid" style="left:240px;top:17px;width:241px;height:115px">
    <h3>Detailing &amp; Hand Wash</h3>
    <ul class="ticks"><li>Comprehensive exterior &amp; interior care</li><li>Personalisation and tailored cleaning packages</li><li>Decontamination</li><li>Premium products</li><li>Attention to detail for a perfect finish</li></ul>
    <div class="pic" role="img" aria-label="Photo: wash mitt cleaning a wheel" style="background:linear-gradient(135deg,#6f7fa8,#c9ccd6 50%,#3b3b3f)"></div>
  </article>
  <article class="card card--mid" style="left:240px;top:140px;width:241px;height:114px">
    <h3>Dry Ice Wash</h3>
    <ul class="ticks"><li>Innovative, waterless method</li><li>Safe for all car parts</li><li>Deep cleans, removes odors</li><li>Allergen-free, antibacterial</li><li>Gentle, effective</li><li>Advanced cleaning technology</li></ul>
    <div class="pic" role="img" aria-label="Photo: dry ice blasting machine" style="background:linear-gradient(135deg,#e8e8e8,#9a9a9a 60%,#2e2e2e)"></div>
  </article>
  <article class="card card--mid" style="left:240px;top:262px;width:241px;height:115px">
    <h3>Ceramic Treatment</h3>
    <ul class="ticks"><li>Durable paint protection</li><li>Water-repellent (hydrophobic) effect</li><li>Easier cleaning, enhanced shine</li><li>Long-term surface safeguarding Shields against</li><li>environmental impacts</li></ul>
    <div class="pic" role="img" aria-label="Photo: gloved hand applying ceramic coating to red paint" style="background:linear-gradient(135deg,#8e1420,#3a0a10 55%,#6b6b70)"></div>
  </article>

  <article class="card card--right" style="left:482px;top:17px;width:240px;height:115px">
    <h3>Covering</h3>
    <ul class="ticks"><li>Personalized vehicle styling</li><li>More than 150 colours available</li><li>Clean cut without using a cutter</li><li>High-quality, durable materials</li><li>Custom designs available</li></ul>
    <div class="pic" role="img" aria-label="Photo: technician applying purple wrap film to a car" style="background:linear-gradient(135deg,#3a3a40,#6a4a8a 60%,#c8c8d0)"></div>
  </article>
  <article class="card card--right" style="left:482px;top:140px;width:240px;height:115px">
    <h3>Detailing Boutique</h3>
    <ul class="ticks"><li>Premium brands available</li><li>Buy on site during your visit</li><li>Essential for at-home car care</li><li>Perfect for quick touch-ups</li></ul>
    <div class="brands">Granite Assembly<br>Pip Autos<br>DRAV Norra</div>
    <div class="pic" role="img" aria-label="Photo: detailing brush cleaning interior trim" style="background:linear-gradient(135deg,#d8d8d8,#7a7a7a 55%,#1c1c1c)"></div>
  </article>
  <article class="card card--right" style="left:482px;top:263px;width:240px;height:114px">
    <h3>Protection Film</h3>
    <ul class="ticks"><li>Invisible, durable shield</li><li>Self-healing technology</li><li>10-year warranty by RQ FOLV</li></ul>
    <div class="pic" role="img" aria-label="Photo: glossy black car bonnet with microfiber towel" style="background:linear-gradient(160deg,#5a6068,#1a1c20 55%,#c47a2a)"></div>
  </article>
  <article class="card card--right" style="left:482px;top:385px;width:240px;height:115px">
    <h3>Polishing</h3>
    <ul class="ticks"><li>Eliminates scratches, holograms</li><li>Revives and protects paint</li><li>Ensures lasting gloss</li><li>Enhances paint life</li><li>Preserves car’s value and beauty</li></ul>
    <div class="pic" role="img" aria-label="Photo: rotary polisher on car paint" style="background:linear-gradient(135deg,#2c5fa8,#4a4a4e 55%,#a0a0a4)"></div>
  </article>

  <div class="strip" role="img" aria-label="Photo: hand holding a rotary polisher with blue pad" style="left:0;width:147px;background:linear-gradient(135deg,#6a6a6e,#1f4f9a 40%,#2a2a2c)"></div>
  <div class="strip" role="img" aria-label="Photo: small polisher working on taped interior trim" style="left:158px;width:149px;background:linear-gradient(135deg,#3a3a3c,#1fa0b0 50%,#d8d2c0)"></div>
  <div class="strip" role="img" aria-label="Photo: brush cleaning a fuel cap area" style="left:319px;width:156px;background:linear-gradient(135deg,#f0f0f0,#9a9a9a 55%,#2a2a2a)"></div>
</section>

</body>
</html>
```